IT Consulting Site Revamping for Marlune

I've put a skeleton together on my website, but realize I need some help (it's http://pilot.marlune-example.ca).
I've pulled together tidbits from other websites, but really need my site to be cleaned up, and really spruced up.
I primarily focus on the IT needs of small to medium size businesses, taking care of everything from their servers and networks down to their workstations.
I also want a page listing the vendors (and logos) that I work with including Quillsoft, Zentrix, Halvor, Brax, TL, RZO, VELK, Trevo, Gatemoor.
There should also be a simple form to get a quote that will email me.
The final design should communicate strength and reliability.
I would like this to be a fully functional website, that I can upload to Plumly Pages, with the same sort of pages that are existing on http://pilot.marlune-example.ca
Updates
Hey everyone,
Hi everyone,
Reason: Hi all,
There are some designers that would like to submit some new designs, so I'm extending the deadline.
Thanks,
Target Market(s)
Small to medium size business owners. This will primarily be males who work in the oil and gas industry.
Industry/Entity Type
Consulting
Look and feel
Each slider illustrates characteristics of the customer's brand and the style your logo design should communicate.

```html
<!DOCTYPE html>
<html lang="en">
<head>
<meta charset="utf-8">
<title>Marlune Solutions – IT Consulting</title>
<link href="https://fonts.googleapis.com/css2?family=Arimo:wght@400;700&family=Ubuntu:wght@300;400&display=swap" rel="stylesheet">
<style>
:root{
  --brand-blue:#1f7fc4;
  --nav-text:#2a6fa8;
  --orange:#f7931e;
  --orange-text:#f07f1a;
  --band:#8fb6d6;
  --pale-blue:#dce9f5;
  --heading-blue:#2c5f8f;
  --body:#444;
  --footer-bg:#ececec;
  --rule:#c9c9c9;
}
*{box-sizing:border-box;margin:0;padding:0}
html,body{width:819px;height:1200px;overflow:hidden;background:#fff}
body{position:relative;font-family:'Arimo',Arial,sans-serif;color:var(--body)}
.abs{position:absolute}
.header{left:0;top:0;width:819px;height:79px;background:#f3f3f3}
.brand{left:103px;top:14px;display:flex;align-items:center;gap:10px}
.brand-mark{width:48px;height:48px;border-radius:50%;background:var(--brand-blue)}
.brand-name{font-family:'Ubuntu',sans-serif;font-weight:400;font-size:36px;color:var(--brand-blue);letter-spacing:-1px}
.phone{left:610px;top:18px;display:flex;align-items:center;gap:8px;font-size:17px;color:var(--brand-blue);white-space:nowrap}
.quote-btn{left:598px;top:45px;width:144px;height:22px;background:var(--orange);color:#fff;font-family:'Ubuntu',sans-serif;font-weight:300;font-size:11.5px;line-height:22px;text-align:center;white-space:nowrap;overflow:hidden}
.nav{left:0;top:79px;width:819px;height:23px;background:linear-gradient(#e2e2e2,#c9c9c9);border-top:1px solid #bbb}
.nav a{position:absolute;top:5px;font-size:11px;color:var(--nav-text);text-decoration:none;white-space:nowrap}
.nav .caret{display:inline-block;border:3.5px solid transparent;border-top:4.5px solid var(--nav-text);margin-left:3px;vertical-align:-2px}
.hero{left:55px;top:110px;width:710px;height:286px;background:linear-gradient(90deg,#e9eef4 0,#f4f7fb 55%,#eef3f9 100%)}
.hero-photo{left:0;top:0;width:360px;height:286px;background:linear-gradient(135deg,#5e6b78,#a9b7c6 45%,#d7e3f0)}
.hero-title{right:22px;top:22px;text-align:right;font-size:29px;font-weight:400;line-height:36px;color:#333;white-space:nowrap}
.hero-text{right:22px;top:97px;text-align:right;font-size:11px;line-height:13px;color:#444;white-space:nowrap}
.hero-btn{left:523px;top:162px;width:167px;height:20px;background:var(--orange);color:#fff;font-family:'Ubuntu',sans-serif;font-size:8.5px;line-height:20px;padding-left:7px;white-space:nowrap;overflow:hidden}
.band{left:53px;top:402px;width:712px;height:47px;background:var(--band);color:#fff;font-size:22px;text-align:center;line-height:45px}
.notch{left:402px;top:396px}
.service h3,.specialists h3{font-family:'Ubuntu',sans-serif;font-weight:400;font-size:12px;color:var(--heading-blue);letter-spacing:.3px;white-space:nowrap}
.service{top:473px;width:160px}
.service ul{list-style:none;margin-top:12px;font-family:'Ubuntu',sans-serif;font-size:9.5px;line-height:14.7px;color:#333;white-space:nowrap}
.learn{position:absolute;top:96px;width:78px;height:20px;background:var(--orange);color:#fff;font-family:'Ubuntu',sans-serif;font-size:9px;line-height:20px;padding-left:7px;white-space:nowrap;overflow:hidden}
.chev{position:absolute;right:6px;top:5px}
.divider{left:82px;top:611px;width:655px;height:1px;background:var(--rule)}
.specialists{left:84px;top:634px;width:197px;height:379px;background:var(--pale-blue);padding:15px 11px}
.specialists p{margin-top:12px;font-family:'Ubuntu',sans-serif;font-size:9.3px;line-height:14.1px;color:#444}
.vendors{display:grid;grid-template-columns:1fr 1fr;row-gap:12px;column-gap:6px;margin-top:20px;font-family:'Ubuntu',sans-serif;font-size:15px;font-weight:400;color:#1d3f73}
.photo{background:linear-gradient(135deg,#6f7c8a,#c6d2de)}
.feature h4{font-family:'Ubuntu',sans-serif;font-weight:400;font-size:12px;color:var(--orange-text)}
.feature p{margin-top:6px;font-family:'Ubuntu',sans-serif;font-size:8.6px;line-height:16px;color:#444}
.footer{left:0;top:1032px;width:819px;height:168px;background:var(--footer-bg);border-top:1px solid #ddd}
.footer-title{font-family:'Ubuntu',sans-serif;font-weight:400;font-size:12px;color:var(--heading-blue);letter-spacing:.3px;white-space:nowrap}
.footer-links{list-style:none;margin-top:9px;font-size:8px;line-height:12px;color:#333}
.social{left:178px;width:87px;height:22px;color:#fff;font-size:9px;font-weight:700;line-height:22px;padding-left:38px;white-space:nowrap}
.social .sq{position:absolute;left:8px;top:5px;width:12px;height:12px;background:rgba(255,255,255,.85)}
.vrule{width:1px;height:127px;top:1050px;background:var(--rule)}
.contact-big{font-family:'Ubuntu',sans-serif;font-size:11.5px;color:#444;white-space:nowrap}
.contact-small{font-size:8px;color:#444;margin-top:2px;white-space:nowrap}
.email{left:541px;top:1077px;width:145px;height:17px;background:#fff;border:1px solid #6aa2d4;font-size:8px;color:#999;line-height:15px;padding-left:5px;white-space:nowrap}
.email-go{left:670px;top:1077px;width:16px;height:17px;background:#2c6fb3}
.news-text{left:541px;top:1104px;width:170px;font-size:8px;line-height:12px;color:#444}
</style>
</head>
<body>
<header class="abs header">
  <div class="abs brand"><span class="brand-mark"></span><span class="brand-name">Marlune</span></div>
  <div class="abs phone">
    <svg width="20" height="20" viewBox="0 0 20 20"><circle cx="10" cy="10" r="9" fill="none" stroke="#1f7fc4" stroke-width="1.6"/><path d="M7 5.5l2 2-1 1.3c.7 1.4 1.8 2.5 3.2 3.2l1.3-1 2 2-1.3 1.5C10 14.5 5.5 10 5.5 6.8z" fill="#1f7fc4"/></svg>
    <span>555 010 2040</span>
  </div>
  <div class="abs quote-btn">GET FREE QUOTE ONLINE</div>
</header>

<nav class="abs nav">
  <a style="left:119px">Home</a>
  <a style="left:197px">About Us</a>
  <a style="left:283px">Services<span class="caret"></span></a>
  <a style="left:366px">Products<span class="caret"></span></a>
  <a style="left:457px">Contact</a>
</nav>
<svg class="abs" style="left:124px;top:96px" width="12" height="7"><path d="M0 7L6 1 12 7z" fill="#fff"/></svg>

<section class="abs hero">
  <div class="abs hero-photo" role="img" aria-label="Photo of two IT professionals shaking hands in a server room"></div>
  <h1 class="abs hero-title">Hidden Network Problems<br>Cost Money</h1>
  <p class="abs hero-text">We can detect hidden network problems<br>and provide ongoing technical support<br>for your small business.</p>
  <div class="abs hero-btn">GET A FREE NETWORK ASSESMENT<svg class="chev" width="6" height="10"><path d="M1 1l4 4-4 4" stroke="#fff" stroke-width="1.8" fill="none"/></svg></div>
</section>

<svg class="abs notch" width="14" height="7"><path d="M0 7L7 0 14 7z" fill="#8fb6d6"/></svg>
<div class="abs band">How can we help your business?</div>

<div class="abs service" style="left:96px">
  <h3>MANAGED IT SERVICES</h3>
  <ul><li>Reduced Downtime</li><li>Improved Productivity</li><li>Innovative Applications</li><li>Critical Data Protection</li></ul>
  <div class="learn">LEARN MORE<svg class="chev" width="6" height="10"><path d="M1 1l4 4-4 4" stroke="#fff" stroke-width="1.8" fill="none"/></svg></div>
</div>
<div class="abs service" style="left:255px">
  <h3>NETWORKING</h3>
  <ul><li>Computer Networking</li><li>Firewalls</li><li>Virtual Private Networks (VPN)</li><li>Remote Access</li></ul>
  <div class="learn">LEARN MORE<svg class="chev" width="6" height="10"><path d="M1 1l4 4-4 4" stroke="#fff" stroke-width="1.8" fill="none"/></svg></div>
</div>
<div class="abs service" style="left:422px">
  <h3>BACK UP &amp; RECOVERY</h3>
  <ul><li>Data Back Up</li><li>Data Recovery</li><li>Storage and Virtualization</li></ul>
  <div class="learn">LEARN MORE<svg class="chev" width="6" height="10"><path d="M1 1l4 4-4 4" stroke="#fff" stroke-width="1.8" fill="none"/></svg></div>
</div>
<div class="abs service" style="left:588px">
  <h3>COMPUTER REPAIR</h3>
  <ul><li>Spyware Removal</li><li>Virus Removal</li><li>On Site Repair Service</li></ul>
  <div class="learn">LEARN MORE<svg class="chev" width="6" height="10"><path d="M1 1l4 4-4 4" stroke="#fff" stroke-width="1.8" fill="none"/></svg></div>
</div>

<div class="abs divider"></div>

<aside class="abs specialists">
  <h3>SMALL BUSINESS SPECIALISTS</h3>
  <p>We've been trusted for over the last 7 years by small business in Calgary for being flexible, easy going, and affordable. We have partnered with the industry giants to provide smart and affordable IT solutions. Our trained and experienced IT professionals deliver rapid issue resolution, ongoing support, maintenance and stability that your business deserves and can depend upon.</p>
  <div class="vendors">
    <span>Quillsoft</span><span>Halvor</span>
    <span>TL</span><span>Brax</span>
    <span>Zentrix</span><span></span>
    <span>VELK</span><span>Gatemoor</span>
    <span>Trevo</span><span>RZO</span>
  </div>
</aside>

<div class="abs photo" style="left:297px;top:636px;width:199px;height:124px" role="img" aria-label="Photo of a technician on the phone beside server racks"></div>
<div class="abs feature" style="left:294px;top:777px;width:205px">
  <h4>Cost Effective</h4>
  <p>Our computer technicians and network professionals understand that your business operations hinge on computer and network availability. Our clients enjoy that our small business support services are flexible, easy and affordable.</p>
</div>
<div class="abs photo" style="left:297px;top:889px;width:199px;height:124px;background:linear-gradient(135deg,#d9dde2,#f4f5f7)" role="img" aria-label="Photo of a smiling support agent wearing a headset"></div>

<div class="abs feature" style="left:523px;top:636px;width:210px">
  <h4>Trusted and Reliable</h4>
  <p>Our trained and experienced IT professionals deliver all day, and every day, rapid issue resolution, ongoing support, maintenance and stability that your business deserves and can depend upon.</p>
</div>
<div class="abs" style="left:521px;top:762px;width:198px;height:124px;background:radial-gradient(circle at 60% 55%,#c8202a 0,#8a1218 22%,#2a2a2a 45%,#111 100%)" role="img" aria-label="Photo of a keyboard with a red Save Money key"></div>
<div class="abs feature" style="left:522px;top:902px;width:215px">
  <h4>Friendly and Simple</h4>
  <p>Our clients love us because we keep technical support simple. We'll make sure you know the important details to keep you on top of things, and handle the complex stuff ourselves, so you can get back to business without the headaches.</p>
</div>

<footer class="abs footer"></footer>
<div class="abs" style="left:101px;top:1055px">
  <h5 class="footer-title">ABOUT US</h5>
  <ul class="footer-links"><li>About Us</li><li>Testimonials</li><li>Technical Blog</li><li>Newsletter</li><li>Contact Us</li></ul>
</div>
<div class="abs social" style="top:1058px;background:#4a6aa8"><span class="sq"></span>Pagewall</div>
<div class="abs social" style="top:1088px;background:#5cb8c9"><span class="sq"></span>Chirpline</div>
<div class="abs social" style="top:1118px;background:#5a5a5a"><span class="sq"></span>Linkwise</div>
<div class="abs vrule" style="left:294px"></div>
<div class="abs" style="left:314px;top:1055px">
  <h5 class="footer-title">CONTACT US</h5>
  <div class="contact-big" style="margin-top:8px">Call 555 010 3050</div>
  <div class="contact-small">24/7 Tech Support</div>
  <div class="contact-big" style="margin-top:12px">Office Location</div>
  <div class="contact-small">PO Box 4417, Calgary, AB, T2T 0A1</div>
</div>
<div class="abs vrule" style="left:516px"></div>
<div class="abs" style="left:541px;top:1055px">
  <h5 class="footer-title">SIGN UP FOR NEWSLETTER</h5>
</div>
<div class="abs email">Your email address...</div>
<div class="abs email-go"><svg width="16" height="17"><path d="M6 5l4 3.5L6 12" stroke="#fff" stroke-width="1.8" fill="none"/></svg></div>
<p class="abs news-text">Read our monthly email newsletter to stay updated on technology that can help you grow your business better.</p>
</body>
</html>
```